Flat Belly Design Graphics for Social

I want to create 9 social media graphics (new Instagram size 4:5 (1080 x 1350 pixels) focusing on our Flat Belly Graphics, using the pics attached. Use the attached pics, NO RANDOM STOCK PHOTOGRAPHY. For the color scheme of the graphics, the color palette is attached. YOU MUST POST ALL 9 GRAPHICS IN ONE ENTRY.
Using the 3 titles below, create one set of graphics. 1) with all text, then for the others, use the pictures as detailed below in IMPORTANT:
1. 21-Night Lean Middle Reboot Beyond 50
2. The 20-Second Trim-Core Menu Guide
3. Starlet Tricks to a Slender Midline Beyond 50 - Zero Scalpel Needed
IMPORTANT:
Only use RK Pic 1 and RK Pic 2 with the title, 21-Night Lean Middle Reboot Beyond 50
Only use meal plan1 and meal plan2 pics with the title, 20-Second Trim-Core Menu Guide
Only use starlet tricks 1 and starlet tricks 2 pics with the title, Starlet Tricks to a Slender Midline Beyond 50 - Zero Scalpel Needed
women over 40

```html
<!DOCTYPE html>
<html lang="en">
<head>
<meta charset="utf-8">
<title>Flat Belly Social Set</title>
<link rel="stylesheet" href="https://fonts.googleapis.com/css2?family=Questrial&display=swap">
<style>
  :root {
    --blush: #fbeef0;
    --rose: #e39ab0;
    --forest: #2f4a48;
    --ink: #141414;
    --white: #ffffff;
  }
  * { margin: 0; padding: 0; box-sizing: border-box; }
  html, body { width: 1200px; height: 750px; overflow: hidden; background: var(--white); }
  body { position: relative; font-family: "Questrial", "Helvetica Neue", Arial, sans-serif; color: var(--forest); }

  .post {
    position: absolute; top: 149px;
    width: 358px; height: 449px;
    border: 2px solid var(--ink);
    background: var(--blush);
    overflow: hidden;
  }
  .post--menu { left: 39px; }
  .post--reboot { left: 423px; }
  .post--tricks { left: 804px; }

  .post__art { position: absolute; inset: 0; width: 354px; height: 445px; display: block; }

  .brand-mark {
    position: absolute; left: 27px; top: 38px; width: 66px; height: 66px;
    display: flex; align-items: center; justify-content: center; text-align: center;
    color: var(--white); font-size: 12px; line-height: 16px; letter-spacing: 0.2px;
  }

  .headline { position: absolute; line-height: 1; white-space: nowrap; }
  .tag {
    position: absolute; background: var(--forest); color: var(--white);
    display: flex; align-items: center; justify-content: center;
    white-space: nowrap; line-height: 1;
  }

  /* Menu guide post */
  .menu-the   { right: 49px; top: 28px; font-size: 25px; }
  .menu-tag   { right: 30px; top: 56px; height: 52px; padding: 0 10px; font-size: 30px; transform: rotate(-1deg); }
  .menu-trim  { right: 30px; top: 116px; font-size: 26px; }
  .menu-guide { right: 20px; top: 144px; font-size: 31px; }

  /* Reboot post */
  .reboot-tag   { right: 59px; top: 29px; height: 47px; padding: 0 14px; font-size: 30px; transform: rotate(-1deg); }
  .reboot-lean  { right: 24px; top: 88px; font-size: 23px; }
  .reboot-age   { right: 23px; top: 114px; font-size: 24px; display: flex; align-items: center; gap: 6px; }
  .age-badge {
    width: 46px; height: 46px; border-radius: 50%; background: var(--forest); color: var(--white);
    display: flex; align-items: center; justify-content: center; font-size: 25px; font-weight: 700;
  }

  /* Tricks post */
  .tricks-starlet { right: 80px; top: 16px; font-size: 24px; }
  .tricks-tag     { right: 55px; top: 42px; height: 43px; padding: 0 12px; font-size: 31px; transform: rotate(-1deg); }
  .tricks-line    { right: 25px; top: 95px; font-size: 20px; }
  .tricks-age     { right: 25px; top: 124px; height: 29px; padding: 0 9px; font-size: 19px; }
  .tricks-note    { right: 25px; top: 160px; font-size: 13px; }
</style>
</head>
<body>

<!-- Post 1: menu guide -->
<section class="post post--menu">
  <svg class="post__art" viewBox="0 0 354 445">
    <defs>
      <linearGradient id="menuTable" x1="0" y1="0" x2="1" y2="1">
        <stop offset="0" stop-color="#7a9a4a"/><stop offset="0.5" stop-color="#4a3328"/><stop offset="1" stop-color="#c6453a"/>
      </linearGradient>
      <radialGradient id="menuBowl" cx="0.5" cy="0.5" r="0.6">
        <stop offset="0" stop-color="#efe6dc"/><stop offset="0.6" stop-color="#8a5a3a"/><stop offset="1" stop-color="#5b3b2a"/>
      </radialGradient>
    </defs>
    <rect class="band" x="0" y="0" width="111" height="445" fill="var(--rose)"/>
    <g role="img" aria-label="Overhead photo of healthy ingredients around a written meal plan on a wooden table">
      <rect x="124" y="283" width="222" height="147" fill="url(#menuTable)" stroke="var(--rose)" stroke-width="2"/>
    </g>
    <circle cx="113" cy="226" r="102" fill="var(--blush)"/>
    <circle cx="113" cy="226" r="87" fill="var(--rose)"/>
    <g role="img" aria-label="Photo of a meal plan sheet with chicken, berries, greens and grains">
      <circle cx="113" cy="226" r="78" fill="url(#menuBowl)"/>
    </g>
    <circle cx="60" cy="71" r="33" fill="none" stroke="var(--white)" stroke-width="1"/>
    <g class="icon-clock" fill="none" stroke="var(--forest)" stroke-width="1.4">
      <circle cx="268" cy="220" r="32"/>
      <path d="M268 200 A20 20 0 0 1 288 220"/>
      <path d="M268 220 V212 M268 220 H285"/>
      <circle cx="268" cy="220" r="1.6" fill="var(--forest)"/>
    </g>
  </svg>
  <div class="brand-mark">YOUR<br>LOGO<br>HERE</div>
  <div class="headline menu-the">The</div>
  <div class="tag menu-tag">20-Second</div>
  <div class="headline menu-trim">Trim-Core</div>
  <div class="headline menu-guide">Menu Guide</div>
</section>

<!-- Post 2: reboot -->
<section class="post post--reboot">
  <svg class="post__art" viewBox="0 0 354 445">
    <defs>
      <linearGradient id="rebootKitchen" x1="0" y1="0" x2="0" y2="1">
        <stop offset="0" stop-color="#8b6a55"/><stop offset="0.45" stop-color="#c9a88e"/><stop offset="1" stop-color="#4a3226"/>
      </linearGradient>
      <linearGradient id="rebootClose" x1="0" y1="0" x2="0" y2="1">
        <stop offset="0" stop-color="#b89276"/><stop offset="0.4" stop-color="#eeeae6"/><stop offset="1" stop-color="#2a1e1a"/>
      </linearGradient>
    </defs>
    <rect class="band" x="0" y="0" width="111" height="445" fill="var(--rose)"/>
    <g role="img" aria-label="Close-up photo of a woman in a white cropped sweater pointing at her waist">
      <rect x="125" y="283" width="220" height="145" fill="url(#rebootClose)" stroke="var(--rose)" stroke-width="2"/>
    </g>
    <circle cx="113" cy="224" r="102" fill="var(--blush)"/>
    <circle cx="113" cy="224" r="87" fill="var(--rose)"/>
    <g role="img" aria-label="Photo of a smiling woman in a kitchen pointing at her flat stomach">
      <circle cx="113" cy="224" r="78" fill="url(#rebootKitchen)"/>
    </g>
    <circle cx="60" cy="71" r="33" fill="none" stroke="var(--white)" stroke-width="1"/>
    <g class="icon-calendar" fill="none" stroke="var(--forest)" stroke-width="1.4">
      <circle cx="273" cy="219" r="32"/>
      <rect x="258" y="204" width="31" height="29" rx="4"/>
      <rect x="258" y="204" width="31" height="6" rx="3" fill="var(--forest)"/>
      <text x="273.5" y="229" text-anchor="middle" font-family="Questrial, sans-serif" font-size="17" fill="var(--forest)" stroke="none">21</text>
    </g>
  </svg>
  <div class="brand-mark">YOUR<br>LOGO<br>HERE</div>
  <div class="tag reboot-tag">21-Night</div>
  <div class="headline reboot-lean">Lean Middle Reboot</div>
  <div class="headline reboot-age">Beyond <span class="age-badge">50</span></div>
</section>

<!-- Post 3: starlet tricks -->
<section class="post post--tricks">
  <svg class="post__art" viewBox="0 0 354 445">
    <defs>
      <linearGradient id="tricksStudio" x1="0" y1="0" x2="1" y2="1">
        <stop offset="0" stop-color="#5cc3d8"/><stop offset="0.55" stop-color="#d9b3a4"/><stop offset="1" stop-color="#4fb4cb"/>
      </linearGradient>
      <linearGradient id="tricksBright" x1="0" y1="0" x2="1" y2="1">
        <stop offset="0" stop-color="#f4f1ee"/><stop offset="0.5" stop-color="#9a6a4e"/><stop offset="1" stop-color="#e9ddd4"/>
      </linearGradient>
    </defs>
    <rect class="band" x="0" y="0" width="111" height="445" fill="var(--rose)"/>
    <g role="img" aria-label="Photo of one woman whispering a secret to a surprised friend outdoors">
      <rect x="124" y="284" width="222" height="146" fill="url(#tricksBright)" stroke="var(--rose)" stroke-width="2"/>
    </g>
    <circle cx="113" cy="226" r="102" fill="var(--blush)"/>
    <circle cx="113" cy="226" r="87" fill="var(--rose)"/>
    <g role="img" aria-label="Photo of two women sharing a secret against a blue backdrop">
      <circle cx="113" cy="226" r="78" fill="url(#tricksStudio)"/>
    </g>
    <circle cx="60" cy="71" r="33" fill="none" stroke="var(--white)" stroke-width="1"/>
    <g class="icon-waist" fill="none" stroke="var(--forest)" stroke-width="1.4">
      <circle cx="269" cy="218" r="32"/>
      <path d="M262 200 C252 212 266 224 258 240"/>
      <path d="M280 198 C268 210 270 228 284 238"/>
    </g>
  </svg>
  <div class="brand-mark">YOUR<br>LOGO<br>HERE</div>
  <div class="headline tricks-starlet">Starlet</div>
  <div class="tag tricks-tag">Tricks</div>
  <div class="headline tricks-line">to a Slender Midline</div>
  <div class="tag tricks-age">Beyond 50</div>
  <div class="headline tricks-note">Zero Scalpel Needed</div>
</section>

</body>
</html>
```